THE COMPANY: FAITHBENCHTALK.COM.AU

"Faith Bench Talk" is a casual and relaxed forum where friends from all walks of life gather for straight talk, hard facts and real answers on our faith and how it applies to daily life.

STYLE:
The feel must be fun, energetic and youthful, and at the same time containing bold undertones, drawing the viewer to connect with the brand and its product.
The look should be warm, modern and up lifting

COLOURS:
There are no restrictions on colours, however there should only be 2 to 3 primary colours throughout the website.

OUTCOME:
The following outputs are required:
- 1 x Logo design
- 1 x Website design and wordpress development
- Website and content management instructions (updating events, contacts, emails, chatterbook & quipper posts etc…)

WEB SITES I LIKE:
Below are the website designs which we would like to influence this project.
- http://www.pelvistream.com
- http://www.brambletrace.com.au/
- http://quillharbour.com.au/
- http://www.dorindavalsh.com/

STRUCTURE:
- Home
- - Sponsor
- - Events
- - - Up coming Events
- - - Historical Events
- - Gallery
- - - Photos
- - - Audio
- - - Videos
- - Donations
- - - General Donations
- - - Event Donations
- - - VIP Donors
- - - Sponsor / Advertise
- - Store
- - - Links to Songvault
- - - Other Links
- - FBT FAQ
- - FBT Friends
- - About Us
- - - Map to Event
- - - Mission
- - - Profile

Target Market(s)

OUR TARGET:
- General public aged 18 to 30
- Religious (i.e. Priests etc…)

KEY WORD: FUN

Industry/Entity Type

It Company

Requirements
Must have
• The site can be developed in wordpress and must be easily administrated

It must be Zorvex and Plov friendly, and allow for key word management, indexing and easy improvement.

The site should have the ability to post and or manage latest Quipper and Chatterbook feed’s

```html
<!DOCTYPE html>
<html lang="en">
<head>
<meta charset="utf-8">
<title>Faith Bench Talk</title>
<link rel="stylesheet" href="https://fonts.googleapis.com/css2?family=Oswald:wght@500;600;700&family=PT+Sans:wght@400;700&display=swap">
<style>
:root{
  --red:#b93b22;
  --red-deep:#c0432c;
  --amber:#f2b233;
  --sand:#f4c97f;
  --card:#2a2a2a;
  --text:#444;
  --blue:#4f6fae;
  --sky:#5bbde6;
  --link:#2f6fb3;
  --white:#fff;
}
*{margin:0;padding:0;box-sizing:border-box}
html,body{width:859px;height:1200px;overflow:hidden}
body{position:relative;background:var(--white);font-family:"PT Sans",Arial,sans-serif;color:var(--text)}
.abs{position:absolute}

.masthead{left:0;top:0;width:859px;height:387px;
  background:radial-gradient(ellipse at 250px 30px,#fac898 0,#f3a577 28%,#ea8155 58%,#d45a3a 85%,#c9472c 100%)}
.brand{left:60px;top:20px;font-family:"Oswald",sans-serif;font-weight:700;font-size:29px;line-height:28px;color:#35251c;letter-spacing:.6px}
.brand span{display:block}
.brand span+span{padding-left:34px;font-weight:600}
.brand-dot{left:226px;top:24px;width:36px;height:36px;border-radius:50%;background:var(--amber);box-shadow:inset 0 -6px 0 rgba(0,0,0,.08)}
.search{left:615px;top:53px;width:187px;height:22px;background:var(--white);border-radius:3px;border:1px solid #e8c3a8;
  font-size:10px;color:#999;padding:5px 9px}
.search svg{position:absolute;right:7px;top:4px}

.mainnav{left:0;top:87px;width:859px;height:36px;background:var(--sand);border-top:1px solid #f8dca0;border-bottom:1px solid #e8b464}
.mainnav ul{list-style:none;position:absolute;left:55px;top:0;display:flex;height:35px}
.mainnav li{font-family:"Oswald",sans-serif;font-weight:500;font-size:14.5px;color:#4a2a1e;padding:0 20px;line-height:35px;border-right:1px solid #e2ab5a;letter-spacing:.2px}
.mainnav li.active{background:var(--red);color:var(--white);padding:0 23px}
.mainnav li:last-child{border-right:none}

.showcase{left:53px;top:132px;width:753px;height:232px;background:var(--white);border-radius:3px;box-shadow:0 1px 3px rgba(0,0,0,.2)}
.slide{left:7px;top:7px;width:519px;height:221px;border-radius:3px;
  background:linear-gradient(180deg,#e4e1dc 0%,#d6d2ca 32%,#b98f70 58%,#7a5540 78%,#3c3434 100%)}
.slide-arrows{right:14px;bottom:8px}
.sponsor-ad{left:533px;top:7px;width:212px;height:221px;background:linear-gradient(165deg,#7cc242 0%,#b6d530 45%,#e3e02a 75%,#95c63c 100%)}
.sponsor-ad .band{position:absolute;left:0;bottom:0;width:100%;height:22px;background:#6fae32}

.section-title{left:54px;top:407px;font-family:"Oswald",sans-serif;font-weight:600;font-size:17px;color:var(--red);letter-spacing:.2px}
.event{width:167px;height:183px}
.event .photo{height:118px}
.event .caption{height:65px;background:var(--card);color:var(--white);padding:9px 6px 0 14px}
.event.featured .caption{background:var(--red)}
.event h3{font-weight:400;font-size:12.5px;letter-spacing:.2px}
.event p{font-size:8.6px;line-height:13px;color:#e3e3e3;margin-top:2px}
.p1{background:linear-gradient(180deg,#f1f1ef 0%,#e5e4e0 55%,#6f86a8 100%)}
.p2{background:linear-gradient(160deg,#6b4a3a 0%,#c9a17e 40%,#d96a52 70%,#4f7fb8 100%)}
.p3{background:linear-gradient(180deg,#5f92c9 0%,#9bbad6 45%,#b98a5e 75%,#3d3328 100%)}
.p4{background:linear-gradient(150deg,#151515 0%,#d7b08f 35%,#f0e8dc 55%,#141414 85%)}
.p5{background:linear-gradient(180deg,#8a4a3a 0%,#c67a4e 40%,#3f78b8 70%,#d2a64c 100%)}
.p6{background:linear-gradient(160deg,#3a2a22 0%,#9b6a48 40%,#d9b15a 70%,#3d5ea8 100%)}
.p7{background:linear-gradient(180deg,#4f7a3a 0%,#b88862 45%,#8a5a44 75%,#6c6a5e 100%)}
.p8{background:linear-gradient(160deg,#2c2620 0%,#7a5a48 40%,#b59482 65%,#3a3230 100%)}
.p9{background:linear-gradient(180deg,#6f9c4a 0%,#a7c46a 35%,#e8b498 60%,#d8566a 85%)}

.feed{left:590px;width:215px;background:var(--white);border:1px solid #e4e4e4;border-radius:3px}
.feed-head{height:35px;color:var(--white);font-size:15px;padding:8px 0 0 37px;position:relative}
.feed-head .mark{position:absolute;left:14px;top:11px;width:12px;height:12px;border-radius:50%;background:var(--white)}
.chatterbook .feed-head{background:var(--blue)}
.quipper .feed-head{background:var(--sky)}
.post{position:relative;height:66px;margin-left:16px}
.post .avatar{position:absolute;left:0;top:12px;width:56px;height:50px;border-radius:3px;box-shadow:0 0 0 1px #e3e3e3}
.post .body{position:absolute;left:66px;top:13px;width:116px}
.post h4{font-weight:400;font-size:10px;color:#222;margin-bottom:1px}
.post p{font-size:8.2px;line-height:13px;color:#666}
.post time{display:block;font-size:8.2px;line-height:13px;color:var(--link)}
.a1{background:linear-gradient(150deg,#6b7a86,#d9cfc6 55%,#8a7a6e)}
.a2{background:linear-gradient(150deg,#2f5a7a,#e0b48c 50%,#8a5a3a)}
.a3{background:linear-gradient(150deg,#7a4a2a,#e8b898 55%,#b87a5a)}
.a4{background:linear-gradient(150deg,#d8e6ee,#e2b894 55%,#6a4a32)}
.a5{background:linear-gradient(150deg,#f1ece6,#e7c17a 50%,#c88a5a)}
.a6{background:linear-gradient(150deg,#c8d0cc,#e9d6c8 55%,#9aa3a4)}

.newsletter{left:590px;top:932px;width:215px;height:102px;border:1px solid #e4e4e4;border-radius:3px;box-shadow:0 0 2px rgba(0,0,0,.08)}
.newsletter h2{position:absolute;left:16px;top:11px;font-weight:400;font-size:15px;color:var(--red)}
.newsletter .field{position:absolute;left:17px;top:37px;width:183px;height:22px;border:1px solid #d8d8d8;border-radius:3px;font-size:9px;color:#888;padding:5px 10px}
.newsletter .btn{position:absolute;right:14px;top:64px;width:71px;height:23px;background:var(--red-deep);border-radius:3px;color:var(--white);font-size:11.5px;text-align:center;line-height:23px}

.footer{left:0;top:1067px;width:859px;height:133px;background:var(--red-deep);color:var(--white)}
.footer-nav{left:56px;top:27px;font-family:"Oswald",sans-serif;font-weight:500;font-size:11px;letter-spacing:.1px;word-spacing:1px}
.copyright{left:56px;top:56px;font-size:10.5px;color:#fbe5dc}
.contact{left:664px;top:27px;font-size:10.5px;line-height:17px;font-style:normal}
.contact strong{font-weight:400;font-size:13.5px}
.social{left:664px;top:90px;display:flex;gap:4px}
.social span{width:16px;height:16px;border-radius:50%;background:var(--white)}
</style>
</head>
<body>

<header class="masthead abs">
  <div class="brand abs"><span>FAITH BENCH</span><span>TALK</span></div>
  <div class="brand-dot abs"></div>
  <div class="search abs">Search here..
    <svg width="13" height="13" viewBox="0 0 13 13"><circle cx="5.5" cy="5.5" r="4" fill="none" stroke="#aaa" stroke-width="1.6"/><line x1="8.5" y1="8.5" x2="12" y2="12" stroke="#aaa" stroke-width="1.8"/></svg>
  </div>

  <nav class="mainnav abs">
    <ul>
      <li class="active">HOME</li><li>EVENTS</li><li>GALLERY</li><li>DONATIONS</li><li>STORE</li><li>FBT FAQ</li><li>FBT FRIENDS</li><li>ABOUT US</li>
    </ul>
  </nav>

  <section class="showcase abs">
    <div class="slide abs" role="img" aria-label="Group of young adults under a shared thought bubble">
      <svg class="slide-arrows abs" width="26" height="14" viewBox="0 0 26 14"><polyline points="8,2 3,7 8,12" fill="none" stroke="#fff" stroke-width="1.8"/><polyline points="18,2 23,7 18,12" fill="none" stroke="#fff" stroke-width="1.8"/></svg>
    </div>
    <div class="sponsor-ad abs" role="img" aria-label="Sponsor advert for Sunvale Fresh Market"><div class="band"></div></div>
  </section>
</header>

<h2 class="section-title abs">UPDATING EVENTS</h2>

<article class="event featured abs" style="left:53px;top:438px"><div class="photo p1" role="img" aria-label="Friends holding up letter shirts"></div><div class="caption"><h3>EVENT NAME</h3><p>Duis tincidunt lectus quis dui viverra Suspendisse vulputate dui.</p></div></article>
<article class="event abs" style="left:229px;top:438px"><div class="photo p2" role="img" aria-label="Friends sharing drinks at a table"></div><div class="caption"><h3>EVENT NAME</h3><p>Duis tincidunt lectus quis dui viverra Suspendisse vulputate dui.</p></div></article>
<article class="event abs" style="left:404px;top:438px"><div class="photo p3" role="img" aria-label="Friends with a guitar outdoors"></div><div class="caption"><h3>EVENT NAME</h3><p>Duis tincidunt lectus quis dui viverra Suspendisse vulputate dui.</p></div></article>

<article class="event abs" style="left:51px;top:642px"><div class="photo p4" role="img" aria-label="Friends lying in a circle"></div><div class="caption"><h3>EVENT NAME</h3><p>Duis tincidunt lectus quis dui viverra Suspendisse vulputate dui.</p></div></article>
<article class="event abs" style="left:228px;top:642px"><div class="photo p5" role="img" aria-label="Crowd at a festival"></div><div class="caption"><h3>EVENT NAME</h3><p>Duis tincidunt lectus quis dui viverra Suspendisse vulputate dui.</p></div></article>
<article class="event abs" style="left:402px;top:642px"><div class="photo p6" role="img" aria-label="Smiling group of young people"></div><div class="caption"><h3>EVENT NAME</h3><p>Duis tincidunt lectus quis dui viverra Suspendisse vulputate dui.</p></div></article>

<article class="event abs" style="left:50px;top:843px"><div class="photo p7" role="img" aria-label="Stacked hands in a team huddle"></div><div class="caption"><h3>EVENT NAME</h3><p>Duis tincidunt lectus quis dui viverra Suspendisse vulputate dui.</p></div></article>
<article class="event abs" style="left:227px;top:843px"><div class="photo p8" role="img" aria-label="Friends greeting each other"></div><div class="caption"><h3>EVENT NAME</h3><p>Duis tincidunt lectus quis dui viverra Suspendisse vulputate dui.</p></div></article>
<article class="event abs" style="left:401px;top:843px"><div class="photo p9" role="img" aria-label="Student reading on the grass"></div><div class="caption"><h3>EVENT NAME</h3><p>Duis tincidunt lectus quis dui viverra Suspendisse vulputate dui.</p></div></article>

<aside class="feed chatterbook abs" style="top:408px;height:251px">
  <div class="feed-head"><span class="mark"></span>Chatterbook Feed</div>
  <div class="post"><div class="avatar a1" role="img" aria-label="Member portrait"></div><div class="body"><h4>Blog Tittle here</h4><p>Duis tincidunt lectus quis dui viverra Suspendisse vulputate</p><time>Posted on May, 18 2013</time></div></div>
  <div class="post"><div class="avatar a2" role="img" aria-label="Member portrait"></div><div class="body"><h4>Blog Tittle here</h4><p>Duis tincidunt lectus quis dui viverra Suspendisse vulputate</p><time>Posted on May, 18 2013</time></div></div>
  <div class="post"><div class="avatar a3" role="img" aria-label="Member portrait"></div><div class="body"><h4>Blog Tittle here</h4><p>Duis tincidunt lectus quis dui</p><time>Posted on May, 18 2013</time></div></div>
</aside>

<aside class="feed quipper abs" style="top:673px;height:250px">
  <div class="feed-head"><span class="mark"></span>Quipper Feed</div>
  <div class="post"><div class="avatar a4" role="img" aria-label="Member portrait"></div><div class="body"><h4>Blog Tittle here</h4><p>Duis tincidunt lectus quis dui viverra Suspendisse vulputate</p><time>May, 10 2013</time></div></div>
  <div class="post"><div class="avatar a5" role="img" aria-label="Member portrait"></div><div class="body"><h4>Blog Tittle here</h4><p>Duis tincidunt lectus quis dui viverra Suspendisse vulputate</p><time>May, 14 2013</time></div></div>
  <div class="post"><div class="avatar a6" role="img" aria-label="Member portrait"></div><div class="body"><h4>Blog Tittle here</h4><p>Duis tincidunt lectus quis dui</p><time>May, 18 2013</time></div></div>
</aside>

<section class="newsletter abs">
  <h2>Newsletter Subscribe</h2>
  <div class="field">email address</div>
  <div class="btn">Subscribe</div>
</section>

<footer class="footer abs">
  <nav class="footer-nav abs">HOME &nbsp;/&nbsp; EVENTS &nbsp;/&nbsp; GALLERY &nbsp;/&nbsp; DONATIONS &nbsp;/&nbsp; STORE &nbsp;/&nbsp; FBT FAQ &nbsp;/&nbsp; FBT FRIENDS &nbsp;/&nbsp; ABOUT US &nbsp;/&nbsp; SPONSORS</nav>
  <p class="copyright abs">Copyright © 2013 Company Name.&nbsp; All right reserved.&nbsp; Term of Use</p>
  <address class="contact abs">482 Harlow Lane #4B<br>Brookfield 20417 NY<br>Phone <strong>(555) 014-7720</strong></address>
  <div class="social abs"><span></span><span></span><span></span><span></span></div>
</footer>

</body>
</html>
```